BrightVale business cards

We want to create two sets of cards. One general card for brightvale [staff] and one card for the founder of the company. Below is the general/basic information for you to format/display on side of the cards:
--Company address: 418 Marlow Street, New York, NY 10034
--Main phone: 212-563-7182
Will also provide you with secondary 1-800 number
--company website: www.brightvale-example.com
--email address for general card: concierge@brightvale-example.com
--email address (for dr lindqvist's card: dr@brightvale-example.com
--titles for dr lindqvist's card: Founder, Medical Director
--Dr. Lindqvist's name on the card should read: Martin E. Lindqvist, MD
You can also play around with brightvale's tag line: Glow Starts With Care (TM or R should be attached as a trademark has been filed)
Reason: More time to design something awesome. This company is an aesthetic medical company that offers cool and safe cosmetic treatments
For the business card design for the doctor, please change the doctor's name to look like this above his title: Martin E. Lindqvist, MD instead of using Dr. Martin....etc
Reason: WILL NOT BE ABLE TO VIEW AND FINALIZE DESIGNS UNTIL I RETURN FROM MEDICAL CONFERENCE, WHICH WILL BE ON SUNDAY/MONDAY. MY APOLOGIES
can everyone try making it very minimalistic
A Bit of a change...
Can everyone take a stab at using a grey "raw" or eco friendly stock paper. We are interested to see the designs you come up with.
Business

```html
<!DOCTYPE html>
<html lang="en">
<head>
<meta charset="utf-8">
<title>BrightVale Business Cards</title>
<link rel="stylesheet" href="https://fonts.googleapis.com/css2?family=Baskervville:wght@400;700&family=Open+Sans:wght@400;600&display=swap">
<style>
  :root {
    --frame: #58585a;
    --sheet: #ffffff;
    --card-edge: #231f20;
    --band-blue: #1b95d3;
    --name-blue: #1f5aa6;
    --logo-blue: #2f86c8;
    --ink: #4d4d4f;
    --grad-top: #d3e9f8;
    --grad-mid: #46b6e8;
    --grad-bottom: #2a6fb8;
    --white: #ffffff;
  }
  * { box-sizing: border-box; margin: 0; padding: 0; }
  html, body { width: 1200px; height: 775px; overflow: hidden; background: var(--frame); }
  .sheet {
    position: absolute; left: 16px; top: 16px; width: 1168px; height: 743px;
    background: var(--sheet);
  }
  .card {
    position: absolute; width: 494px; height: 282px;
    border: 1px solid var(--card-edge); background: var(--sheet); overflow: hidden;
  }
  .card--founder { left: 53px; top: 58px; }
  .card--general { left: 614px; top: 58px; }
  .card--back-left { left: 53px; top: 400px; }
  .card--back-right { left: 614px; top: 400px; }

  .web-band {
    position: absolute; left: 0; top: 16px; width: 54px; height: 250px;
    background: var(--band-blue);
    display: flex; align-items: center; justify-content: center;
  }
  .web-band span {
    writing-mode: vertical-rl; transform: rotate(180deg);
    font-family: "Open Sans", sans-serif; font-size: 12.5px; letter-spacing: 0.04em;
    color: var(--white); white-space: nowrap;
  }
  .details {
    position: absolute; left: 77px;
    font-family: "Baskervville", serif; font-size: 14.5px; color: var(--ink); line-height: 20px;
    font-variant-numeric: lining-nums;
    white-space: nowrap;
  }
  .card--founder .details { top: 36px; }
  .card--general .details { top: 74px; }
  .name {
    font-family: "Baskervville", serif; font-weight: 700; font-size: 21px;
    color: var(--name-blue); line-height: 24px; letter-spacing: 0.01em;
  }
  .title {
    font-family: "Open Sans", sans-serif; font-size: 12.5px; letter-spacing: 0.05em;
    text-transform: uppercase; color: var(--ink); line-height: 18px; margin-bottom: 20px;
  }
  .address { margin-bottom: 20px; }
  .phones { line-height: 25px; }
  .email { line-height: 25px; }
  .card--general .address { margin-bottom: 18px; }
  .card--general .email { margin-top: 6px; }

  .wordmark {
    position: absolute; font-family: "Baskervville", serif; font-weight: 400;
    color: var(--logo-blue); letter-spacing: -0.01em; line-height: 1;
  }
  .wordmark sup { font-size: 0.25em; vertical-align: top; position: relative; top: 0.3em; margin-left: 2px; }
  .card--founder .wordmark { right: 18px; top: 208px; font-size: 32px; }
  .card--general .wordmark { right: 18px; top: 184px; font-size: 32px; }

  .back-field {
    position: absolute; left: 17px; top: 16px; width: 477px; height: 250px;
    background: linear-gradient(to bottom, var(--grad-top) 0%, var(--grad-mid) 50%, var(--grad-bottom) 100%);
    display: flex; flex-direction: column; align-items: center; justify-content: center;
    color: var(--white);
  }
  .back-field .wordmark {
    position: static; color: var(--white); font-size: 66px; letter-spacing: -0.02em;
  }
  .tagline {
    font-family: "Open Sans", sans-serif; font-size: 8.5px; letter-spacing: 0.28em;
    text-transform: uppercase; margin-top: 6px; color: var(--white);
  }
</style>
</head>
<body>
<main class="sheet">
  <section class="card card--founder">
    <div class="web-band"><span>WWW.BRIGHTVALE-EXAMPLE.COM</span></div>
    <div class="details">
      <p class="name">Martin E. Lindqvist, MD</p>
      <p class="title">Founder, Medical Director</p>
      <p class="address">418 Marlow Street<br>New York, NY 10034</p>
      <p class="phones">212.563.7182<br>1.800.000.0000</p>
      <p class="email">dr@brightvale-example.com</p>
    </div>
    <p class="wordmark">brightvale<sup>®</sup></p>
  </section>

  <section class="card card--general">
    <div class="web-band"><span>WWW.BRIGHTVALE-EXAMPLE.COM</span></div>
    <div class="details">
      <p class="address">418 Marlow Street<br>New York, NY 10034</p>
      <p class="phones">212.563.7182<br>1.800.000.0000</p>
      <p class="email">concierge@brightvale-example.com</p>
    </div>
    <p class="wordmark">brightvale<sup>®</sup></p>
  </section>

  <section class="card card--back-left">
    <div class="back-field">
      <p class="wordmark">brightvale<sup>®</sup></p>
      <p class="tagline">Glow Starts With Care™</p>
    </div>
  </section>

  <section class="card card--back-right">
    <div class="back-field">
      <p class="wordmark">brightvale<sup>®</sup></p>
      <p class="tagline">Glow Starts With Care™</p>
    </div>
  </section>
</main>
</body>
</html>
```